Design a Flat design copy of this flyer

Copy the brochure but use flat design instead of 3D.
Copy placement of items.

Winning designer will be awarded website development work for word press site.

```html
<!DOCTYPE html>
<html lang="en">
<head>
<meta charset="utf-8">
<title>NVX. Flyer</title>
<link rel="stylesheet" href="https://fonts.googleapis.com/css2?family=Arimo:wght@400;700&display=swap">
<style>
:root{
  --panel-blue:#3f5c9c;
  --band-dark:#262626;
  --card-white:#ffffff;
  --card-shadow:rgba(0,0,0,.35);
  --ink:#333333;
  --ink-soft:#555555;
  --tick-green:#3e9a3a;
  --accent-yellow:#f1b51c;
  --accent-blue:#3f5c9c;
  --toggle-grey:#e6e6e6;
  --toggle-dark:#3a3a3a;
  --toggle-green:#36b53a;
}
*{box-sizing:border-box;margin:0;padding:0}
html,body{width:843px;height:1200px;overflow:hidden;background:var(--panel-blue)}
body{font-family:"Arimo",Arial,sans-serif;color:var(--ink);position:relative}
.panel{position:absolute;left:0;width:843px;background:var(--panel-blue)}
.panel--top{top:0;height:520px}
.panel--bottom{top:598px;height:522px}
.band{position:absolute;left:0;width:843px;background:var(--band-dark);color:#fff;text-align:center;font-weight:700;font-size:15px;line-height:20px}
.band--top{top:520px;height:78px;padding-top:19px}
.band--bottom{top:1120px;height:80px;padding-top:17px}
.brand{position:absolute;left:36px;width:60px;height:60px;border:2px solid #ccc;background:#5a4f8f;color:#fff;font-weight:700;font-size:17px;display:flex;align-items:center;justify-content:center}
.card{position:absolute;background:var(--card-white);border-radius:9px;box-shadow:2px 3px 4px var(--card-shadow)}
.nav{display:flex;align-items:center;font-size:15px;color:var(--ink-soft)}
.nav span{text-align:center;border-left:1px solid #aaa;line-height:24px;white-space:nowrap}
.nav span:first-child{border-left:0}
.icon{position:absolute;width:42px;height:42px;border-radius:50%;background:#fff;border:4px solid;display:flex;align-items:center;justify-content:center}
.icon svg{width:20px;height:20px}
.tag{position:absolute;height:30px;background:#fff;clip-path:polygon(14px 0,100% 0,100% 100%,14px 100%,0 50%);font-size:12.5px;display:flex;align-items:center;justify-content:center;padding-left:12px;color:#222;white-space:nowrap}
.tag b{color:var(--accent-yellow)}
.toggle{position:absolute;left:682px;top:103px;width:124px;height:37px;border-radius:6px;background:var(--toggle-grey);border:2px solid #999;overflow:hidden}
.toggle span{position:absolute;right:0;top:0;width:62px;height:100%;background:var(--toggle-dark);color:var(--toggle-green);font-weight:700;font-size:14px;display:flex;align-items:center;justify-content:center}
.list{list-style:none;font-size:14px;line-height:20.7px;color:var(--ink-soft)}
.list li{white-space:nowrap}
.list li::before{content:"✓ ";color:var(--tick-green);font-weight:700}
.offer h3{font-size:15.5px;color:var(--ink-soft);margin-bottom:1px}
.tail{position:absolute;width:18px;height:18px;background:#fff;transform:rotate(45deg)}
.art{position:absolute;border-radius:6px}
.tech{display:flex;align-items:center;font-size:16px;color:var(--ink-soft)}
.tech span{text-align:center;border-left:1px solid #aaa;line-height:22px;white-space:nowrap}
.tech span:first-child{border-left:0}
.build .list{line-height:20px}
.build .list li{margin-bottom:8px;padding-left:18px;text-indent:-18px}
.hl{font-weight:700;color:var(--accent-blue)}
.partner{position:absolute;background:rgba(255,255,255,.8);border-radius:4px}
.tagline{display:flex;align-items:center;justify-content:center;font-size:16px;color:#666;white-space:nowrap}
.tagline strong{margin-right:5px}
</style>
</head>
<body>

<section class="panel panel--top">
  <div class="brand" style="top:44px">NVX.</div>
  <nav class="card nav" style="left:237px;top:45px;width:570px;height:35px">
    <span style="width:109px">Privacy</span><span style="width:111px">Security</span><span style="width:187px">Multiple Languages</span><span style="width:163px">Personalisation</span>
  </nav>

  <div class="icon" style="left:37px;top:124px;border-color:#3a7ec2"><svg viewBox="0 0 20 20"><circle cx="10" cy="7" r="4" fill="#555"/><path d="M3 18c0-4 3-6 7-6s7 2 7 6z" fill="#555"/></svg></div>
  <div class="tag" style="left:85px;top:131px;width:160px">Friends, Family, Contacts</div>
  <div class="icon" style="left:37px;top:176px;border-color:#3a7ec2"><svg viewBox="0 0 20 20"><path d="M10 2 2 10h3v8h10v-8h3z" fill="#555"/></svg></div>
  <div class="tag" style="left:85px;top:183px;width:160px">Properties</div>
  <div class="icon" style="left:37px;top:229px;border-color:#8b3a8f"><svg viewBox="0 0 20 20"><path d="M10 2 2 10h3v8h10v-8h3z" fill="#555"/></svg></div>
  <div class="tag" style="left:85px;top:235px;width:160px">Utilities</div>
  <div class="icon" style="left:37px;top:281px;border-color:#7bb241"><svg viewBox="0 0 20 20"><path d="M2 10a8 8 0 0 1 16 0z" fill="#555"/><path d="M10 10v6a2 2 0 0 1-4 0" stroke="#555" stroke-width="1.6" fill="none"/></svg></div>
  <div class="tag" style="left:85px;top:287px;width:160px">Insurances</div>
  <div class="icon" style="left:37px;top:333px;border-color:#f1b51c"><svg viewBox="0 0 20 20"><rect x="2" y="8" width="16" height="6" rx="2" fill="#555"/><rect x="5" y="4" width="10" height="5" rx="1.5" fill="#555"/><circle cx="6" cy="15" r="2" fill="#555"/><circle cx="14" cy="15" r="2" fill="#555"/></svg></div>
  <div class="tag" style="left:85px;top:339px;width:160px">Vehicles</div>

  <div class="icon" style="left:294px;top:124px;border-color:#f1b51c"><svg viewBox="0 0 20 20"><rect x="2" y="5" width="16" height="10" rx="1" fill="#555"/><circle cx="10" cy="10" r="2.5" fill="#fff"/></svg></div>
  <div class="tag" style="left:343px;top:131px;width:146px">Financial</div>
  <div class="icon" style="left:294px;top:176px;border-color:#d0346a"><svg viewBox="0 0 20 20"><path d="M2 11l16-6-5 12-3-5z" fill="#555"/></svg></div>
  <div class="tag" style="left:343px;top:183px;width:146px">Travel</div>
  <div class="icon" style="left:294px;top:229px;border-color:#d0346a"><svg viewBox="0 0 20 20"><path d="M10 17 3 10a4 4 0 0 1 7-5 4 4 0 0 1 7 5z" fill="#555"/></svg></div>
  <div class="tag" style="left:343px;top:235px;width:146px">Biometrics</div>
  <div class="icon" style="left:294px;top:281px;border-color:#2aa7a0"><svg viewBox="0 0 20 20"><ellipse cx="10" cy="9" rx="8" ry="6" fill="#555"/><path d="M5 13l-2 4 5-2z" fill="#555"/></svg></div>
  <div class="tag" style="left:343px;top:287px;width:146px">Notifications</div>
  <div class="icon" style="left:294px;top:333px;border-color:#f1d21c"><svg viewBox="0 0 20 20"><rect x="3" y="6" width="9" height="8" rx="2" fill="#555"/><path d="M12 8h5M12 12h5" stroke="#555" stroke-width="2"/></svg></div>
  <div class="tag" style="left:343px;top:339px;width:146px"><b>API</b>&nbsp;Designer / Plugin</div>

  <div class="toggle"><span>Opt In</span></div>

  <div class="tail" style="left:741px;top:297px"></div>
  <div class="card offer" style="left:534px;top:164px;width:272px;height:141px;padding:11px 15px">
    <h3>Offering users:</h3>
    <ul class="list">
      <li>Transparent Opt in Process</li>
      <li>Smart Search</li>
      <li>Organise and link your personal data</li>
      <li>Left &amp; Right hand Smart Interface</li>
      <li>Buying Power</li>
    </ul>
  </div>

  <div class="art" role="img" aria-label="Ring of colourful figures holding hands above a short caption" style="left:35px;top:392px;width:105px;height:113px;background:radial-gradient(circle,#5a8bd0 0%,#5a7fc0 70%,transparent 72%)"></div>

  <div class="tail" style="left:481px;top:397px"></div>
  <div class="card" style="left:183px;top:393px;width:307px;height:113px;padding:4px 10px">
    <ul class="list" style="line-height:20.8px">
      <li>Establish your needs, wants &amp; wishes</li>
      <li>Make your money go further</li>
      <li>User ranked product suppliers</li>
      <li>Providing the tools you need</li>
      <li>Smart Recommendations specified by you</li>
    </ul>
  </div>

  <div class="art" role="img" aria-label="Two white figures standing beside a large glossy product title" style="left:512px;top:328px;width:294px;height:190px;background:linear-gradient(180deg,#4e69a8,#7f97cf)"></div>
</section>

<footer class="band band--top">
  <p>T: +44 (0) 20 7946 0321</p>
  <p>www.northvaleworks.com</p>
</footer>

<section class="panel panel--bottom">
  <div class="brand" style="top:44px">NVX.</div>
  <nav class="card tech" style="left:187px;top:47px;width:619px;height:38px">
    <span style="width:77px">NoSQL</span><span style="width:69px">Lens</span><span style="width:64px">Band</span><span style="width:65px">QDSB</span><span style="width:53px">SMS</span><span style="width:96px">Scan Beam</span><span style="width:53px">OCR</span><span style="width:142px">Speech to Text</span>
  </nav>

  <div class="card build" style="left:37px;top:131px;width:418px;height:179px;padding:7px 14px">
    <ul class="list">
      <li>Use our <span class="hl">D</span>rag &amp; <span class="hl">D</span>rop <span class="hl">S</span>creen <span class="hl">B</span>uilder to quickly create your<br>own system, or pick from our available business templates.</li>
      <li>Customise to your specfic needs.</li>
      <li>Integrate with Providers &amp; Suppliers using our API bank, if<br>the API isn’t available, then we will build it!</li>
      <li>React to market changes. You can change the business<br>rules, work flow or data management, you are in control.</li>
    </ul>
  </div>

  <div class="card" style="left:538px;top:131px;width:268px;height:97px;padding:8px 10px">
    <ul class="list" style="line-height:20.5px">
      <li>Accessible from Desktop,<br>&nbsp;&nbsp;&nbsp;&nbsp;Tablet &amp; Mobile with your own app</li>
      <li>Energy Efficient</li>
      <li><span class="hl">F</span>lexible <span class="hl">E</span>ntity <span class="hl">L</span>inking</li>
    </ul>
  </div>

  <div class="art" role="img" aria-label="Glossy box graphic with a large product title and an orange arrow" style="left:537px;top:270px;width:225px;height:162px;background:linear-gradient(180deg,#e9eef6,#c7d1e2)"></div>

  <div class="partner" style="left:40px;top:365px;width:100px;height:28px"></div>
  <div class="partner" style="left:157px;top:352px;width:78px;height:48px"></div>
  <div class="partner" style="left:248px;top:362px;width:106px;height:32px"></div>
  <div class="partner" style="left:378px;top:350px;width:80px;height:56px;border-radius:50%"></div>

  <div class="card tagline" style="left:37px;top:448px;width:769px;height:48px">
    <strong>Integration and Development made easy.</strong> Create software that works for you!
  </div>
</section>

<footer class="band band--bottom">
  <p>T: +44 (0) 20 7946 0321</p>
  <p>www.northvaleworks.com</p>
</footer>

</body>
</html>
```